Industrial & commercial facility maintenance flyer

Design a 2 sided flyer that outlines our core business unit services. One side shall be for our industrial maintenance division while the other will be focused on our commercial maintenance division.

Media from website here: https://files.velnorashare.com/folders/7K3QzP91mXwRtLaBvYcNe4HdUsFj

Target Market(s)

Industrial and commercial facility maintenance companies and professionals

Industry/Entity Type

Maintenance

Font styles to use
Serif

Colors
ffffff
2f73b4
0455a3
cfdfed

Requirements
Must have
• Several photos of each applicable service. Reference existing website (www.tkrvb.com). Use of the blue and grey scheme of our current logo.
Nice to have
• Our logo design across the top with our contact information on the bottom.

```html
<!DOCTYPE html>
<html lang="en">
<head>
<meta charset="utf-8">
<title>Ridgeline Maintenance Solutions – Facility Maintenance Flyer</title>
<link rel="stylesheet" href="https://fonts.googleapis.com/css2?family=Oswald:wght@500;600&family=Questrial&family=Montserrat:ital,wght@0,500;0,600;1,500&display=swap">
<style>
:root{
  --white:#ffffff;
  --blue:#0455a3;
  --blue-mid:#2f73b4;
  --blue-pale:#cfdfed;
  --grey:#5e6670;
  --grey-light:#c9ced3;
  --ink:#2b2f33;
  --stage:#dcdee0;
}
*{margin:0;padding:0;box-sizing:border-box}
html,body{width:1200px;height:3398px;overflow:hidden;background:var(--stage)}
.sheet{position:absolute;left:43px;width:1119px;background:var(--white);overflow:hidden}
.sheet--industrial{top:43px;height:1589px}
.sheet--commercial{top:1709px;height:1646px}
.sheet-art{position:absolute;left:0;top:0;width:100%;height:100%}
.abs{position:absolute}
.headline{font-family:'Oswald',sans-serif;font-weight:600;color:var(--blue);text-transform:uppercase;line-height:1.12}
.tagline{font-family:'Montserrat',sans-serif;font-style:italic;font-weight:500;color:var(--blue);}
.section-title{font-family:'Oswald',sans-serif;font-weight:500;text-transform:uppercase;line-height:1.15}
.body-copy{font-family:'Questrial',sans-serif;font-size:12.6px;line-height:1.32;color:var(--ink)}
.body-copy p+p{margin-top:10px}
.on-blue{color:var(--white)}
.sub-title{font-family:'Montserrat',sans-serif;font-weight:600;font-size:25px;color:var(--white)}
.web-link{font-family:'Montserrat',sans-serif;font-style:italic;font-weight:500;font-size:28px;color:var(--white)}
.brand{display:flex;align-items:center;gap:14px}
.brand-mark{width:80px;height:80px;border-radius:50%;background:var(--grey);flex:none}
.brand-name{font-family:'Montserrat',sans-serif;font-weight:500;font-size:33px;color:var(--blue);line-height:1}
.brand-line{font-family:'Montserrat',sans-serif;font-weight:500;font-size:12.5px;letter-spacing:4.4px;color:var(--grey);margin-top:8px;border-top:2px solid var(--grey-light);padding-top:5px}
.social{display:flex;align-items:center;gap:12px}
.social-label{font-family:'Montserrat',sans-serif;font-weight:600;font-size:29px;color:var(--blue);margin-right:6px}
.social-dot{width:50px;height:50px;border-radius:50%;background:var(--blue)}
</style>
</head>
<body>

<!-- Industrial division side -->
<section class="sheet sheet--industrial">
  <svg class="sheet-art" viewBox="0 0 466 662" preserveAspectRatio="none">
    <defs>
      <linearGradient id="skyline" x1="0" y1="0" x2="1" y2="0">
        <stop offset="0" stop-color="#b9c6d4"/><stop offset="1" stop-color="#ffffff"/>
      </linearGradient>
      <linearGradient id="worker" x1="0" y1="0" x2="1" y2="1">
        <stop offset="0" stop-color="#2a55a8"/><stop offset="1" stop-color="#6d7f99"/>
      </linearGradient>
      <linearGradient id="plant" x1="0" y1="0" x2="0" y2="1">
        <stop offset="0" stop-color="#a8a69a"/><stop offset="1" stop-color="#6c6f6b"/>
      </linearGradient>
      <linearGradient id="team" x1="0" y1="0" x2="0" y2="1">
        <stop offset="0" stop-color="#c8a14a"/><stop offset="1" stop-color="#7a6a5a"/>
      </linearGradient>
    </defs>
    <rect x="230" y="0" width="140" height="150" fill="url(#skyline)" role="img" aria-label="Faded city skyline"/>
    <polygon points="0,0 232,0 232,140 0,168" fill="url(#worker)" role="img" aria-label="Technician in blue coveralls holding a wrench"/>
    <polygon points="0,170 466,92 466,108 0,190" fill="var(--blue)"/>
    <polygon points="0,196 466,116 466,124 0,204" fill="var(--blue-pale)"/>
    <polygon points="0,208 148,184 148,345 0,365" fill="#3d5c9a" role="img" aria-label="Gloved hands tightening a fitting with a wrench"/>
    <polygon points="156,182 304,158 304,325 156,345" fill="url(#plant)" role="img" aria-label="Industrial machinery interior"/>
    <polygon points="312,156 466,130 466,300 312,322" fill="#8f9a92" role="img" aria-label="Factory production hall"/>
    <polygon points="0,370 466,300 466,336 0,408" fill="var(--blue)"/>
    <polygon points="0,408 466,336 466,360 0,420" fill="var(--grey)"/>
    <polygon points="0,420 466,360 466,662 0,662" fill="var(--white)"/>
    <rect x="180" y="250" width="252" height="172" rx="40" fill="url(#team)" role="img" aria-label="Group of maintenance workers in hard hats with toolboxes"/>
    <rect x="17" y="400" width="212" height="192" fill="var(--blue)"/>
    <rect x="0" y="652" width="229" height="10" fill="var(--blue)"/>
  </svg>

  <h1 class="headline abs" style="left:612px;top:48px;width:480px;font-size:42px;text-align:center">Facility Maintenance &amp; Management Solutions</h1>
  <p class="tagline abs" style="left:612px;top:148px;width:480px;font-size:28px;text-align:center">“Maintaining Your Business”</p>

  <div class="abs" style="left:62px;top:1005px;width:460px">
    <h2 class="section-title on-blue" style="font-size:27px">Industrial Maintenance Solutions</h2>
    <p class="body-copy on-blue" style="margin-top:10px">Our industrial maintenance teams work in the field to handle your needs as quickly as possible, whether to get your critical broken or malfunctioning equipment going again or to support scheduled downtime. We specialize in industrial maintenance, conveyor repair, and overhead door repair, but our industrial services aren’t limited to those services. Others include equipment repairs, installation, and adjustment, just to name a few.</p>
    <h3 class="sub-title" style="margin-top:26px">Get Your Maintenance Solution</h3>
    <p class="body-copy on-blue" style="margin-top:4px">We greatly appreciate you taking the time to visit our website. Feel free to reach out using the form on this page and we will be in touch as soon as we can. We look forward to hearing from you!</p>
    <p class="web-link" style="margin-top:20px">www.tkrvb.com</p>
  </div>

  <div class="brand abs" style="left:48px;top:1448px">
    <span class="brand-mark"></span>
    <div>
      <div class="brand-name">Ridgeline Maintenance</div>
      <div class="brand-line">INDUSTRIAL · COMMERCIAL · RETAIL</div>
    </div>
  </div>

  <div class="abs" style="left:570px;top:1068px;width:540px">
    <h2 class="section-title" style="font-size:25px;color:var(--blue)">Industrial Maintenance Services You Can Rely On</h2>
    <div class="body-copy" style="margin-top:8px">
      <p>Ridgeline Maintenance Solutions has been Atlanta’s trusted industrial and commercial maintenance solution for over 10 years. Our industrial teams are available 24/7 for equipment maintenance, installation, or repair, and can be onsite within 4 hours.</p>
      <p>We provide conveyor system repair and overhead door repair and maintenance, but our services don’t end there. We cater to your needs to provide exactly what services you want. Other services we offer include plant maintenance, equipment installation and relocation, and repairs of all types of process and manufacturing equipment. In addition to the physical element of industrial maintenance, we also offer facility safety consultations.</p>
      <p>Ridgeline Maintenance Solutions has teams of welders, millwrights, mechanics, carpenters, and more standing ready to support your operation. The welders are certified and provide fabrication for all of your needs, such as carbon steel, stainless steel, structural steel, sheet metal, aluminum, and chrome alloy. Both the millwrights and mechanics safely move, assemble, and install machinery, taking special care with exact positioning and rigging. They also dismantle, move, and overhaul equipment and machinery.</p>
      <p>We provide equipment repair services to many local industries. Services include repair of bearing bores, repair/replacement of worn shafts and production equipment, hydraulic system repair, broken bolt removal, and much more.</p>
    </div>
  </div>

  <div class="social abs" style="left:700px;top:1510px">
    <span class="social-label">Follow us on</span>
    <span class="social-dot"></span><span class="social-dot"></span><span class="social-dot"></span>
  </div>
</section>

<!-- Commercial division side -->
<section class="sheet sheet--commercial">
  <svg class="sheet-art" viewBox="0 0 466 686" preserveAspectRatio="none">
    <defs>
      <linearGradient id="tower" x1="0" y1="0" x2="0" y2="1">
        <stop offset="0" stop-color="#ffffff"/><stop offset="1" stop-color="#9aa6b3"/>
      </linearGradient>
      <linearGradient id="mall" x1="0" y1="0" x2="0" y2="1">
        <stop offset="0" stop-color="#3f6fb0"/><stop offset="1" stop-color="#5a4a55"/>
      </linearGradient>
    </defs>
    <polygon points="0,0 246,0 246,226 0,262" fill="#7d8790" role="img" aria-label="Technician with tool belt stepping out of a service van"/>
    <rect x="246" y="48" width="220" height="178" fill="var(--blue)"/>
    <polygon points="0,268 466,198 466,212 0,282" fill="var(--blue-pale)"/>
    <polygon points="0,290 154,266 154,430 0,452" fill="#b9b4a6" role="img" aria-label="Technician in hard hat servicing a ceiling unit"/>
    <polygon points="160,265 306,242 306,408 160,429" fill="#8e9aa3" role="img" aria-label="Plumber inspecting a sink"/>
    <polygon points="312,241 466,216 466,386 312,407" fill="url(#mall)" role="img" aria-label="Shopping centre storefronts at dusk"/>
    <polygon points="0,455 466,388 466,420 0,490" fill="var(--blue)"/>
    <polygon points="0,490 466,420 466,440 0,506" fill="var(--grey)"/>
    <polygon points="0,506 466,440 466,686 0,686" fill="var(--white)"/>
    <polygon points="0,506 225,472 225,686 0,686" fill="url(#tower)" role="img" aria-label="Glass office tower seen from below"/>
  </svg>

  <div class="brand abs" style="left:615px;top:48px">
    <span class="brand-mark" style="width:70px;height:70px"></span>
    <div>
      <div class="brand-name" style="font-size:29px">Ridgeline Maintenance</div>
      <div class="brand-line" style="font-size:11px;letter-spacing:3.6px">INDUSTRIAL · COMMERCIAL · RETAIL</div>
    </div>
  </div>

  <div class="abs" style="left:640px;top:195px;width:440px">
    <h2 class="section-title on-blue" style="font-size:36px;line-height:1.25">Retail &amp; Commercial Maintenance Solutions</h2>
    <p class="body-copy on-blue" style="margin-top:14px">Ridgeline Maintenance Solutions knows how important it is to convert window shoppers to paying customers and to move inventory off your shelves. We ensure that your business is always looking its best with our cost-effective maintenance programs and crews available 24/7 to take care of any equipment or facility malfunction as quickly as possible.</p>
  </div>

  <div class="abs" style="left:552px;top:1155px;width:540px">
    <h2 class="section-title" style="font-size:35px;color:var(--blue)">Retail Maintenance Services<br>You Can Rely On</h2>
    <div class="body-copy" style="margin-top:12px;font-size:13px">
      <p>Ridgeline Maintenance Solutions provides services to stand-alone stores and big box stores alike, malls, nightclubs, and more. We work to enhance your image by taking preventative measures, like inspecting equipment for signs of wear or failing components. We service equipment as needed, measuring either by usage or manufacturer recommendations. After maintenance and repairs, our technicians provide an in-depth report on equipment conditions, analyze equipment failure, and discuss future prevention.</p>
      <p>Customers may not realize how much work and effort goes into maintaining a functional well-kept business, but Ridgeline Maintenance does. For your convenience, we offer a vast range of services to handle any issues that may occur or to help you expand your business, whether adding on to your existing location or moving to a new one.</p>
      <p>We install doors, restroom partitions, storefronts, flooring, and plumbing. Repairs include doors, storefronts, flooring, building exteriors, plumbing, appliances, fencing, and loading docks. We take care of landscaping, snow removal, irrigation systems, pest control, and other seasonal maintenance as need be when the weather changes.</p>
    </div>
  </div>

  <div class="social abs" style="left:55px;top:1427px">
    <span class="social-label">Follow us on</span>
    <span class="social-dot"></span><span class="social-dot"></span><span class="social-dot"></span>
  </div>
</section>

</body>
</html>
```